label design for coffee bean packaging

Logo will be provided. Label design for package of coffee beans for a micro roasted coffee company. Need to have space to write in origin, weight with check box for 1/4, 1/2, 1lb. Need to have check boxes for Light, Medium, Dark. Creative unique label design with boarders and fun, modern design. Company name is Cedar Brook Roasting Company. See attached logo. I have source files for logo if needed for design.
Industry/Entity Type
Coffee Shop
Font styles to use
Other font styles liked:
- Montez, kautiva cyrillic, uniform bold
Colors
f78f20
faa54b
f37122
fece3e
acd036
Requirements
Must have
- logo included in the design

```html
<!DOCTYPE html>
<html lang="en">
<head>
<meta charset="utf-8">
<title>Cedar Brook Roasting Company – Coffee Bag Label</title>
<link href="https://fonts.googleapis.com/css2?family=Felipa&family=Ubuntu:wght@400;500&display=swap" rel="stylesheet">
<style>
  :root {
    --roast-brown: #5c2c13;
    --label-white: #ffffff;
    --ink: #1e1a17;
    --leaf-grey: #d9d9d9;
    --leaf-light: #f3f3f3;
    --stage: #efe9e3;
  }
  * { box-sizing: border-box; margin: 0; padding: 0; }
  html, body {
    width: 1200px; height: 1200px; overflow: hidden;
    background: var(--stage);
  }
  .label {
    position: absolute; left: 231px; top: 145px;
    width: 738px; height: 910px;
    background: var(--roast-brown);
    font-family: "Ubuntu", sans-serif;
  }
  .side-panel {
    position: absolute; top: 34px; width: 86px; height: 840px;
    border: 2px solid var(--label-white);
    outline: 6px solid var(--roast-brown);
    outline-offset: -10px;
    background: linear-gradient(180deg, var(--leaf-light), var(--leaf-grey) 45%, var(--leaf-light) 70%, var(--leaf-grey));
  }
  .side-panel--left { left: 34px; }
  .side-panel--right { right: 34px; }
  .center-panel {
    position: absolute; left: 120px; top: 0;
    width: 498px; height: 910px;
    background: var(--label-white);
  }
  .brand-seal {
    position: absolute; left: 39px; top: 82px;
    width: 424px; height: 424px;
    border: 5px solid var(--roast-brown);
    border-radius: 50%;
    display: flex; flex-direction: column; align-items: center; justify-content: center;
    color: var(--roast-brown);
    font-weight: 500;
    text-align: center;
  }
  .brand-seal__name { font-size: 52px; line-height: 1.1; }
  .brand-seal__sub { font-size: 28px; line-height: 1.3; letter-spacing: 0.5px; }
  .origin-name {
    position: absolute; left: 0; width: 100%; top: 542px;
    text-align: center;
    font-family: "Felipa", cursive;
    font-size: 66px; color: var(--roast-brown);
  }
  .roast-options {
    position: absolute; left: 58px; top: 648px;
    display: flex; gap: 34px;
    font-size: 24px; color: var(--ink);
  }
  .roast-options span, .weight-options span { display: flex; align-items: center; }
  .checkbox {
    display: inline-block; width: 19px; height: 19px;
    border: 1.5px solid var(--ink); margin-right: 3px;
  }
  .date-roasted {
    position: absolute; left: 58px; top: 722px;
    font-size: 26px; color: var(--ink);
  }
  .weight-band {
    position: absolute; left: 0; top: 762px;
    width: 100%; height: 82px;
    background: var(--roast-brown);
    color: var(--label-white);
    padding: 4px 0 0 58px;
  }
  .weight-band__title { font-size: 26px; }
  .weight-options { display: flex; gap: 40px; font-size: 26px; margin-top: 4px; }
  .checkbox--filled {
    width: 19px; height: 19px; background: var(--label-white);
    border: none; margin-right: 10px;
  }
  .rule {
    position: absolute; left: 0; top: 848px; width: 100%;
    height: 3px; background: var(--roast-brown);
  }
  .web-address {
    position: absolute; left: 0; width: 100%; top: 862px;
    text-align: center; font-size: 19px; color: var(--roast-brown);
  }
</style>
</head>
<body>
  <div class="label">
    <div class="side-panel side-panel--left" role="img" aria-label="Engraved coffee leaf illustration in light grey"></div>
    <div class="side-panel side-panel--right" role="img" aria-label="Engraved coffee leaf illustration in light grey"></div>

    <div class="center-panel">
      <div class="brand-seal">
        <div class="brand-seal__name">Cedar Brook</div>
        <div class="brand-seal__sub">Roasting Company</div>
      </div>

      <div class="origin-name">Origin Name</div>

      <div class="roast-options">
        <span><i class="checkbox"></i>LIGHT</span>
        <span><i class="checkbox"></i>MEDIUM</span>
        <span><i class="checkbox"></i>DARK</span>
      </div>

      <div class="date-roasted">Date Roasted:</div>

      <div class="weight-band">
        <div class="weight-band__title">Net. Wight:</div>
        <div class="weight-options">
          <span><i class="checkbox checkbox--filled"></i>1/4</span>
          <span><i class="checkbox checkbox--filled"></i>1/2</span>
          <span><i class="checkbox checkbox--filled"></i>1lb</span>
        </div>
      </div>

      <div class="rule"></div>
      <div class="web-address">www.cedarbrookroastingcompany.com</div>
    </div>
  </div>
</body>
</html>
```